The WILLOW Lodge is a transitional living housue for women in recovery. It is structured and loving an

I have uploaded my old brochure which was not designed professionally. I want a fresh, funky feel. Our website is www.willowlodgeofthecedarshores.com if you want to get ideas from that but I do not like the bubbles on it. I have uploded a few pics of the houses and the backyards. Please help us convey love and hope and recovery!

```html
<!DOCTYPE html>
<html lang="en">
<head>
<meta charset="utf-8">
<title>Willow Lodge of the Cedar Shores</title>
<link rel="stylesheet" href="https://fonts.googleapis.com/css2?family=Pacifico&family=Nunito:wght@400;700;800&display=swap">
<style>
  :root {
    --plum: #5f2d60;
    --plum-deep: #4a2050;
    --charcoal: #333333;
    --rose: #c7628f;
    --rose-soft: #e596b8;
    --lime: #b6dc4a;
    --aqua: #33c9e6;
    --cream: #fff8f0;
    --white: #ffffff;
    --ink: #3a2a3c;
  }
  * { box-sizing: border-box; margin: 0; padding: 0; }
  html, body { width: 994px; height: 1200px; overflow: hidden; }
  body {
    position: relative;
    background: var(--cream);
    font-family: "Nunito", "Helvetica Neue", Arial, sans-serif;
  }

  .masthead { position: absolute; left: 0; top: 0; width: 994px; height: 177px; background: var(--plum); overflow: hidden; }
  .stripe-row { position: absolute; left: 0; width: 994px; display: flex; }
  .stripe-row.top { top: 0; height: 52px; }
  .stripe-row.bottom { top: 124px; height: 53px; }
  .stripe-row span { flex: 0 0 71px; height: 100%; }
  .stripe-row span:nth-child(3n+1) { background: var(--plum); }
  .stripe-row span:nth-child(3n+2) { background: var(--charcoal); }
  .stripe-row span:nth-child(3n) { background: var(--plum-deep); }

  .title-band {
    position: absolute; left: 0; top: 52px; width: 994px; height: 72px;
    background: var(--rose);
    display: flex; align-items: center; justify-content: center;
  }
  .title-band::before, .title-band::after {
    content: ""; position: absolute; left: 0; right: 0;
    border-top: 2px dashed rgba(255,255,255,0.85);
  }
  .title-band::before { top: 6px; }
  .title-band::after { bottom: 6px; }
  .brand-name {
    font-family: "Pacifico", cursive;
    font-weight: 400; font-size: 36px; line-height: 1;
    color: var(--white); padding-bottom: 6px;
  }

  .hero-photo {
    position: absolute; left: 0; top: 194px; width: 994px; height: 300px;
    background: linear-gradient(175deg, #2f5a2a 0%, #4f8a3a 30%, #6fb7a8 55%, #29bde0 75%, #7fd6ea 100%);
  }

  .intro-panel {
    position: absolute; left: 0; top: 508px; width: 653px; height: 421px;
    background: var(--rose);
    border-top: 8px solid var(--lime);
    padding: 46px 30px 0 30px;
  }
  .intro-text { color: var(--ink); font-size: 18px; line-height: 28px; font-weight: 400; }

  .contact-panel {
    position: absolute; left: 0; top: 946px; width: 653px; height: 254px;
    background: var(--charcoal);
    color: var(--white);
    display: flex; flex-direction: column; align-items: center;
    padding-top: 53px; text-align: center;
    font-size: 20px; line-height: 28px; font-weight: 400;
  }
  .contact-panel .contact-title { font-weight: 800; color: var(--rose-soft); }
  .contact-panel .phone { margin-top: 28px; font-weight: 700; color: var(--lime); }

  .gallery {
    position: absolute; left: 670px; top: 508px; width: 324px; height: 692px;
    background: var(--plum);
  }
  .gallery-photo {
    position: absolute; left: 47px; width: 236px;
    border: 7px solid var(--white); border-radius: 14px;
  }
  .gallery-photo.house-green { top: 15px; height: 213px; background: linear-gradient(160deg, #4f7d3a 0%, #a8d64a 55%, #8a6aa8 100%); }
  .gallery-photo.house-blue { top: 248px; height: 211px; background: linear-gradient(180deg, #f4f2d8 0%, #a9c0dc 55%, #c9d6ea 100%); }
  .gallery-photo.garden-path { top: 476px; height: 201px; background: linear-gradient(170deg, #e9d9a8 0%, #8f9a4a 50%, #6a7a3a 100%); }
</style>
</head>
<body>
  <header class="masthead">
    <div class="stripe-row top">
      <span></span><span></span><span></span><span></span><span></span><span></span><span></span><span></span><span></span><span></span><span></span><span></span><span></span><span></span>
    </div>
    <div class="title-band">
      <h1 class="brand-name">Willow Lodge of the Cedar Shores</h1>
    </div>
    <div class="stripe-row bottom">
      <span></span><span></span><span></span><span></span><span></span><span></span><span></span><span></span><span></span><span></span><span></span><span></span><span></span><span></span>
    </div>
  </header>

  <div class="hero-photo" role="img" aria-label="Backyard pool surrounded by tropical plants and patio chairs"></div>

  <section class="intro-panel">
    <p class="intro-text">Located in the Artisan district of tropical downtown Harbor Bay, FL are our recovery homes, a place for serious women to utilize our comprehensive program based on "old-school" recovery and a wealth of resources. We have built a dynamic program as unique as each woman who lives here. We foster the love, understanding, structure and discipline required to build a strong foundation for long-term recovery from substance abuse. It is much more than sober living; it is an integrative, successful approach to recovery that has yet to be replicated.</p>
  </section>

  <section class="contact-panel">
    <p class="contact-title">Contact Us</p>
    <p>2950 Marigold Ave. N.</p>
    <p>Harbor Bay, FL 30987</p>
    <p class="phone">555-018-4327</p>
  </section>

  <aside class="gallery">
    <div class="gallery-photo house-green" role="img" aria-label="Lime green cottage with purple trim and a picket fence"></div>
    <div class="gallery-photo house-blue" role="img" aria-label="Light blue house with a red door behind a white picket fence"></div>
    <div class="gallery-photo garden-path" role="img" aria-label="Wooden garden walkway through sunlit greenery"></div>
  </aside>
</body>
</html>
```